Accounting Practice Business Card Design

I have a logo I am happy for you to use in the design of the Business Card.
You can edit and change colours as you please, I am not fixated on it.
I am looking for a modern and clean overall feel for the finished design.

The business is a small accounting practice who thrives on word of mouth referrals and this card will be given to all current and prospect clients.

Industry/Entity Type

Accountant

Contact Information for Business Card

Marcus Elwin
Level 5, 8 Corvale Ridge Road
ASHGROVE RISE VIC 3187
Phone: 9481 3057
Email: melwin@mrfaccountants.com.au
Web: www.mrfaccountants.com.au

Font styles to use
Serif
Sans Serif

Colors
0555a3
3277b5
85acd3
0393ce
33a6d7
85cae6
00a990
33b8a4
9bcb3c

Requirements
Must have
• "The end to your tax problems begin with us"
• "A referral from you is our greatest compliment"
Nice to have
• Modern clean professional

```html
<!DOCTYPE html>
<html lang="en">
<head>
<meta charset="utf-8">
<title>MRF Accountants – Business Card</title>
<link rel="stylesheet" href="https://fonts.googleapis.com/css2?family=Roboto+Condensed:wght@400;700&display=swap">
<style>
  :root {
    --stage-centre: #05606e;
    --stage-edge: #0a2f3e;
    --card-navy: #0b5374;
    --card-navy-deep: #094766;
    --band-teal: #0e7885;
    --brand-blue: #1f82c4;
    --accent-green: #7dc242;
    --text-light: #e8eef2;
    --text-muted: #d4e4ea;
    --tagline: #85cae6;
    --paper: #ffffff;
  }
  * { margin: 0; padding: 0; box-sizing: border-box; }
  html, body { width: 1200px; height: 820px; overflow: hidden; }
  body {
    background: radial-gradient(ellipse 70% 75% at 50% 40%, var(--stage-centre) 0%, #074a5a 55%, var(--stage-edge) 100%);
    font-family: "Roboto Condensed", "Arial Narrow", sans-serif;
    position: relative;
  }
  .card {
    position: absolute;
    top: 256px;
    width: 488px;
    height: 275px;
    box-shadow: 6px 8px 10px rgba(0, 0, 0, 0.55);
    overflow: hidden;
  }

  /* Front */
  .card--front { left: 91px; height: 274px; }
  .front__texture {
    position: absolute;
    inset: 0;
    background: linear-gradient(135deg, #0c5a7c 0%, var(--card-navy) 55%, var(--card-navy-deep) 100%);
  }
  .wordmark {
    position: absolute;
    left: 0; right: 0;
    top: 108px;
    text-align: center;
    color: var(--brand-blue);
    font-weight: 700;
    font-size: 40px;
    line-height: 1;
    letter-spacing: 0.5px;
  }
  .taglines {
    position: absolute;
    left: 0; right: 0;
    bottom: 22px;
    text-align: center;
    color: var(--tagline);
    font-size: 11px;
    line-height: 1.5;
    letter-spacing: 0.6px;
    text-transform: uppercase;
  }

  /* Back */
  .card--back {
    left: 615px;
    background: var(--paper);
    padding: 9px 0;
  }
  .back__band { position: relative; overflow: hidden; }
  .back__band--name { height: 88px; background: var(--card-navy); }
  .back__band--contact { height: 129px; background: var(--band-teal); }
  .back__band--web { height: 40px; background: var(--card-navy); }

  .holder {
    position: absolute;
    top: 30px; left: 0; right: 0;
    text-align: center;
    font-weight: 700;
    font-size: 27px;
    line-height: 1;
    letter-spacing: 0.5px;
    color: var(--text-light);
  }
  .holder__first { color: var(--accent-green); }
  .holder__rule {
    position: absolute;
    left: 85px; width: 310px; top: 60px; height: 1px;
    background: linear-gradient(90deg, transparent, rgba(255,255,255,0.85), transparent);
  }

  .contact-grid {
    position: absolute;
    left: 31px; top: 14px;
    width: 429px; height: 100px;
    display: flex;
    border: 1px solid rgba(220, 235, 240, 0.55);
  }
  .contact-cell {
    flex: 1;
    display: flex;
    flex-direction: column;
    align-items: center;
    justify-content: center;
    text-align: center;
    color: var(--text-muted);
    font-size: 9.5px;
    letter-spacing: 0.4px;
    line-height: 1.15;
    text-transform: uppercase;
  }
  .contact-cell + .contact-cell { border-left: 1px solid rgba(220, 235, 240, 0.55); }
  .contact-cell svg { display: block; margin-bottom: 8px; }
  .contact-cell--mail svg { margin-bottom: 6px; }

  .web {
    position: absolute;
    top: 0; left: 0; right: 0; height: 40px;
    line-height: 42px;
    text-align: center;
    color: var(--text-light);
    font-size: 20px;
    letter-spacing: 0.6px;
  }
  .web strong { font-weight: 700; }
</style>
</head>
<body>

  <section class="card card--front" aria-label="Card front">
    <div class="front__texture" role="img" aria-label="Fine diagonal line texture in soft blue over the navy card"></div>
    <p class="wordmark">MRF ACCOUNTANTS</p>
    <div class="taglines">
      <p>The end to your tax problems begin with us</p>
      <p>A referral from you is our greatest compliment</p>
    </div>
  </section>

  <section class="card card--back" aria-label="Card back">
    <div class="back__band back__band--name">
      <h1 class="holder"><span class="holder__first">MARCUS</span> ELWIN</h1>
      <div class="holder__rule"></div>
    </div>

    <div class="back__band back__band--contact">
      <div class="contact-grid">
        <div class="contact-cell contact-cell--address">
          <svg width="28" height="24" viewBox="0 0 28 24" aria-hidden="true">
            <path d="M14 1 L27 12 L24 12 L24 23 L17 23 L17 16 L11 16 L11 23 L4 23 L4 12 L1 12 Z" fill="#ffffff"/>
          </svg>
          <span>Level 5, 8 Corvale Ridge Road</span>
          <span>Ashgrove Rise VIC 3187</span>
        </div>
        <div class="contact-cell contact-cell--mail">
          <svg width="24" height="17" viewBox="0 0 24 17" aria-hidden="true">
            <rect x="0.5" y="0.5" width="23" height="16" fill="#ffffff"/>
            <path d="M1 1 L12 10 L23 1" stroke="var(--band-teal)" stroke-width="1.4" fill="none"/>
          </svg>
          <span>(613) 9481 3057</span>
          <span>melwin@mrfaccountants.com.au</span>
        </div>
      </div>
    </div>

    <div class="back__band back__band--web">
      <p class="web">WWW.<strong>MRFACCOUNTANTS</strong>.COM.AU</p>
    </div>
  </section>

</body>
</html>
```